Veterinary Hospital Brochure - 2 Drafts - 1 Normal and 1 Fun.

Meadowbrook Pet Hospital needs a brochure to promote our veterinary hospital. These will be delivered to local mailboxes. I would like to see atleast 2 submissions from each designer.
One submission conservative and A4 folded DL and another submission more radical and interesting with innovative folding or crazy concepts. Maybe the brochure could be designed to fold into a dog house ?
I want at least one version to be VERY SIMPLE AND INTIMATE.
Our existing website is here: http://furlane.example/ and our new website will look like this: http://trial4.pagemint.example/#home
Please use colors and images from the new website, and information from the old website. The heading font used in the new site is Qorvatype - Otter Tilt Sketchline
I want the brochure to be simple and engaging on first view, and then provide the opportunity to find more information if desired. The brochure needs to be captivating on the outside so people don't throw it away immediately.

We will soon need letterhead, flags, pens, business cards, signs and vouchers so there is the opportunity for more work for the successful designer.

Target Market(s)

Women 25 to 44

Industry/Entity Type

Veterinary

Contact Information for Business Card

Meadowbrook Pet Hospital
14 Marlow Crescent
Tamsworth Vale
NSW 2417
Phone: 02 61938205
Emergency: 0417360592
Fax: 02 83159462
www.meadowbrookvets.example
contact@meadowbrookvets.example

Font styles to use
Script

Requirements
Must have
• Colors from the new website: http://meadowbrookvets.example/ and new logo.
• Information from the old website: http://furlane.example/
• 2 drafts - A normal A4 folded DL flyer and an interesting crazy design.
Nice to have
• VERY SIMPLE
• Subdued
• Intimate
Should not have
• Intense colours
• Red

```html
<!DOCTYPE html>
<html lang="en">
<head>
<meta charset="utf-8">
<title>Meadowbrook Pet Hospital – Tri-fold Brochure</title>
<link href="https://fonts.googleapis.com/css2?family=Mulish:wght@400;600;700;800&family=Handlee&display=swap" rel="stylesheet">
<style>
:root{
  --canvas:#e6e6e6;
  --paper:#ffffff;
  --paper-shade:#f1f1f1;
  --orange:#f08a4b;
  --green:#8cc63f;
  --brown:#4a3222;
  --ink:#3c3c3c;
  --muted:#5a5a5a;
}
*{margin:0;padding:0;box-sizing:border-box}
html,body{width:800px;height:1200px;overflow:hidden;background:var(--canvas)}
body{position:relative;font-family:"Mulish",Arial,sans-serif;color:var(--ink)}
.spread{position:absolute;left:46px;width:709px;height:505px;overflow:hidden;background:var(--paper)}
.spread--outside{top:80px}
.spread--inside{top:615px}
.panel{position:absolute;top:0;height:100%}
.fold-shade{position:absolute;top:0;height:100%;width:24px;background:linear-gradient(90deg,rgba(0,0,0,.06),rgba(0,0,0,0))}
.abs{position:absolute}
.center{text-align:center}
.brand{font-weight:800;color:var(--brown);font-size:17px;line-height:1.1;text-align:center;letter-spacing:.2px}
.brand small{display:block;font-size:11px;letter-spacing:1px}
.script{font-family:"Handlee",cursive}
.small{font-size:10.5px;line-height:15px;color:var(--muted)}
.intro{font-size:9.4px;line-height:11.5px;color:var(--muted)}
.photo{position:absolute}
.quote{font-size:10px;line-height:15.5px;color:var(--muted)}
.quote-mark{color:var(--orange);font-weight:800;font-size:16px;line-height:0}
.signature{font-size:14px;color:var(--ink)}
.caption{font-size:8.5px;font-weight:700;line-height:11px;text-align:center}
.hours{position:absolute;left:293px;top:287px;width:118px;height:76px;border:1.5px solid var(--green);border-radius:8px;text-align:center;font-size:9.5px;line-height:13px;color:var(--muted)}
.hours h3{position:absolute;top:-11px;left:50%;transform:translateX(-50%);background:var(--paper);padding:0 5px;font-family:"Handlee",cursive;font-weight:400;font-size:14px;color:var(--orange);white-space:nowrap}
.hours b{color:var(--ink);font-weight:600}
.tagline{font-size:21px;color:var(--orange);line-height:29px;text-align:center}
.photo-url{font-size:9.5px;font-weight:700;color:#fff}
.services-band{position:absolute;left:257px;top:19px;width:452px;height:25px;background:var(--green);border-radius:13px 0 0 13px}
.services-band h2{font-family:"Handlee",cursive;font-weight:400;font-size:17px;color:#fff;line-height:25px;padding-left:52px}
.service{position:absolute;width:170px}
.service-icon{position:absolute;left:-37px;top:-6px;width:24px;height:24px;border-radius:50%;background:var(--orange)}
.service h4{font-size:10.5px;font-weight:700;color:var(--orange);line-height:13px;margin-bottom:5px}
.service p{font-size:9.2px;line-height:11.5px;color:var(--muted)}
.book{position:absolute;left:78px;top:441px;width:92px;height:21px;border-radius:11px;background:var(--green);color:#fff;font-size:11px;line-height:21px;text-align:center}
.partner{position:absolute;left:296px;top:445px;width:128px;height:30px}
</style>
</head>
<body>

<!-- Outside spread -->
<section class="spread spread--outside">
  <div class="fold-shade" style="left:236px"></div>
  <div class="fold-shade" style="left:472px"></div>

  <!-- Left panel -->
  <svg class="photo" style="left:0;top:0" width="290" height="290" viewBox="0 0 290 290" role="img" aria-label="Photo of a puppy giving a high five to a young woman on a sunny field">
    <defs><linearGradient id="sunField" x1="0" y1="0" x2="1" y2="1"><stop offset="0" stop-color="#f3dcc0"/><stop offset=".5" stop-color="#d7ab7a"/><stop offset="1" stop-color="#a77a52"/></linearGradient></defs>
    <path d="M0 0H268C276 40 280 90 270 140C262 175 245 195 218 200C212 225 200 260 185 268C170 275 160 255 160 230C150 255 135 262 122 250C110 235 112 215 108 205C80 212 40 214 0 208Z" fill="url(#sunField)"/>
    <path d="M268 0C276 40 280 90 270 140C262 175 245 195 218 200C212 225 200 260 185 268C170 275 160 255 160 230C150 255 135 262 122 250C110 235 112 215 108 205C80 212 40 214 0 208" fill="none" stroke="var(--orange)" stroke-width="1" stroke-dasharray="4 3" transform="translate(5 6)"/>
  </svg>

  <p class="quote abs" style="left:17px;top:303px;width:200px"><span class="quote-mark">“</span> Meadowbrook Pet Hospitals friendly, qualified and caring team help families and their pets. We want to make sure your pet is as healthy and happy as they can be by creating a comfortable and inviting environment where you feel part of our family and receive ongoing support. <span class="quote-mark">”</span></p>
  <p class="signature script abs center" style="left:0;width:236px;top:432px">Clare Hadley (BVSc)</p>
  <p class="caption abs" style="left:0;width:236px;top:458px">Veterinarian (BVSc) Hospital Superintendant.<br>Hospital Owner.</p>

  <!-- Middle panel -->
  <div class="brand abs" style="left:236px;width:236px;top:70px"><small>MEADOWBROOK PET</small>HOSPITAL</div>
  <p class="small abs center" style="left:236px;width:236px;top:133px">14 Marlow Crescent,<br>Tamsworth Vale NSW 2417</p>
  <p class="small abs center" style="left:236px;width:236px;top:168px">Phone 02 61938205<br>Emergency 0417360592</p>
  <p class="small abs center" style="left:236px;width:236px;top:211px">contact@meadowbrookvets.example<br>www.meadowbrookvets.example</p>
  <div class="hours">
    <h3>Open hours</h3>
    <p style="margin-top:13px"><b>Monday to Friday</b><br>8:30am to 5:30pm</p>
    <p style="margin-top:4px"><b>Saturday</b><br>9:00am to 12:00 midday</p>
  </div>
  <p class="abs center" style="left:236px;width:236px;top:464px;font-size:9.5px;font-weight:600">meadowbrookvets</p>

  <!-- Right panel -->
  <div class="brand abs" style="left:472px;width:237px;top:70px"><small>MEADOWBROOK PET</small>HOSPITAL</div>
  <p class="tagline script abs" style="left:472px;width:237px;top:144px">Kindness,<br>when you need it most</p>
  <svg class="photo" style="left:400px;top:220px" width="309" height="285" viewBox="0 0 309 285" role="img" aria-label="Photo of a woman hugging her dog">
    <defs><linearGradient id="hugTone" x1="0" y1="0" x2="1" y2="1"><stop offset="0" stop-color="#dfe9d0"/><stop offset=".5" stop-color="#c9b79a"/><stop offset="1" stop-color="#6e5643"/></linearGradient></defs>
    <path d="M309 285H45C50 250 40 225 55 200C30 195 40 160 68 160C75 135 85 110 95 95C100 70 110 40 125 35C140 30 145 55 148 70C155 40 170 40 175 65C180 80 190 85 205 80C215 60 235 60 240 90C250 110 270 120 290 140C300 170 309 200 309 230Z" fill="url(#hugTone)"/>
    <path d="M45 278C50 245 35 220 48 195C22 190 32 152 62 153C70 128 80 103 90 88C95 62 105 30 123 27C142 23 146 48 148 62C157 32 174 33 179 58C185 72 194 76 203 72C215 50 238 52 245 85C256 104 276 114 296 135" fill="none" stroke="var(--orange)" stroke-width="1" stroke-dasharray="4 3"/>
  </svg>
  <p class="photo-url abs" style="left:512px;top:465px">www.meadowbrookvets.example</p>
</section>

<!-- Inside spread -->
<section class="spread spread--inside">
  <div class="panel" style="left:0;width:242px;background:linear-gradient(180deg,#fff,var(--paper-shade))"></div>
  <div class="fold-shade" style="left:242px"></div>
  <div class="fold-shade" style="left:472px"></div>

  <!-- Left panel -->
  <div class="brand abs" style="left:0;width:242px;top:55px"><small>MEADOWBROOK PET</small>HOSPITAL</div>
  <p class="intro abs" style="left:25px;top:104px;width:212px">Meadowbrook Pet Hospital is a Companion Animal Veterinary Hospital in Tamsworth Vale committed to providing excellent care for loved pets and their owners.</p>
  <p class="intro abs" style="left:25px;top:156px;width:212px">We treat Dog, Cats, Reptiles, Rodents, Birds, and other little critters. As a companion animal only Hospital, we are dedicated to improving the wellbing of your beloved pets.</p>
  <svg class="photo" style="left:0;top:210px" width="242" height="222" viewBox="0 0 242 222" role="img" aria-label="Photo of a tabby cat sitting on a lap indoors">
    <defs><linearGradient id="catTone" x1="0" y1="0" x2="1" y2="1"><stop offset="0" stop-color="#e9e2d9"/><stop offset=".5" stop-color="#9b8c7c"/><stop offset="1" stop-color="#4b4038"/></linearGradient></defs>
    <path d="M0 10H150C165 -5 195 0 200 25C230 25 245 55 230 80C245 100 240 135 215 140C220 170 200 200 170 195C150 220 110 220 95 195C70 205 40 195 35 170H0Z" fill="url(#catTone)"/>
    <path d="M0 4H148C165 -10 200 -5 205 20C236 22 252 55 236 80C252 102 246 140 220 145C224 178 202 208 172 202C150 226 108 226 92 202C66 212 34 200 30 176H0" fill="none" stroke="var(--green)" stroke-width="1" stroke-dasharray="4 3"/>
  </svg>
  <div class="book">Book online</div>
  <p class="small abs center" style="left:0;width:242px;top:470px">www.meadowbrookvets.example</p>

  <!-- Services -->
  <div class="services-band"><h2>Our Services</h2></div>

  <div class="service" style="left:296px;top:65px"><span class="service-icon"></span><h4>Companion Animal Surgery</h4><p>Meadowbrook Pet Hospital has the latest surgical instrumentation and anaesthetic monitoring to ensure the success of surgery and outcomes for your pets.</p></div>
  <div class="service" style="left:296px;top:154px"><span class="service-icon"></span><h4>Puppy School</h4><p>Puppy Pre-School is an essential first step for all puppies regardless of breed or owner education.</p></div>
  <div class="service" style="left:296px;top:221px"><span class="service-icon"></span><h4>Laboratory</h4><p>Lorem ipsum dolor sit amet, consectetur adipiscing elit. Ut eget congue orci. Maecenas et luctus lacus.</p></div>
  <div class="service" style="left:296px;top:292px"><span class="service-icon"></span><h4>Feline Friendly</h4><p>Lorem ipsum dolor sit amet, consectetur adipiscing elit. Ut eget congue orci. Maecenas et luctus lacus.</p></div>
  <div class="service" style="left:296px;top:366px"><span class="service-icon"></span><h4>Complimentary Nail Clipping</h4><p>Meadowbrook Pet hospital provides nail clipping. All we ask is a note donation to Helping Paws Australia.</p></div>
  <svg class="partner" viewBox="0 0 128 30" role="img" aria-label="Partner badge"><rect x="0" y="2" width="26" height="26" rx="4" fill="#3a8fd0"/><rect x="32" y="8" width="90" height="14" rx="3" fill="#cfe3f3"/></svg>

  <div class="service" style="left:526px;top:65px"><span class="service-icon"></span><h4>Companion Animal Medecine</h4><p>Our diagnostic facilities enable us to identify disease rapidly and treat promptly with the correct therapies.</p></div>
  <div class="service" style="left:526px;top:137px"><span class="service-icon"></span><h4>Follow Ups and Reminders</h4><p>Lorem ipsum dolor sit amet, consectetur adipiscing elit. Ut eget congue orci. Maecenas et luctus lacus.</p></div>
  <div class="service" style="left:526px;top:206px"><span class="service-icon"></span><h4>Radiology and Ultrasound</h4><p>Lorem ipsum dolor sit amet, consectetur adipiscing elit. Ut eget congue orci. Maecenas et luctus lacus.</p></div>

  <svg class="photo" style="left:462px;top:280px" width="247" height="225" viewBox="0 0 247 225" role="img" aria-label="Photo of two vets examining a large dog on the floor">
    <defs><linearGradient id="vetTone" x1="0" y1="0" x2="1" y2="1"><stop offset="0" stop-color="#f3e2c8"/><stop offset=".5" stop-color="#b58c63"/><stop offset="1" stop-color="#3d3530"/></linearGradient></defs>
    <path d="M247 225H20C0 200 5 160 35 150C25 120 50 95 80 100C85 60 120 40 150 50C170 20 215 15 235 45C247 60 247 80 247 90Z" fill="url(#vetTone)"/>
    <path d="M14 220C-6 195 -2 155 28 144C18 114 44 88 74 94C80 54 117 32 148 44C168 12 216 8 238 38" fill="none" stroke="var(--green)" stroke-width="1" stroke-dasharray="4 3"/>
  </svg>
</section>

</body>
</html>
```